Business Cards Needed For Veterinary Business

Looking for a business card design for a veterinary blood bank. We would like it to be clean and professional on appearance but still warm and inviting. We would like to utilize our logo and similar coloring. We will use our phone number, email, website, employee name, employee title.

We do not want a bunch of animated animal photos but do not need the style to be as clinical as a laboratory or human medical procedure office.

We are looking for some creative ideas to choose from so that we can generate a standout professional business card for our management team to utilize.

Target Market(s)

professionals

Industry/Entity Type

veterinary

Contact Information for Business Card

employee name, employee title, phone number, website URL, email

Font styles to use
Sans Serif

Colors
0054AA
0677BA
7BADD7
CADEEF
E8F1F8
EB3D1F
EC4F4E
F09395
F8D3D4
FCEDEE

Requirements
Nice to have
• creative design
Should not have
• animated photos

```html
<!DOCTYPE html>
<html lang="en">
<head>
<meta charset="utf-8">
<title>Northfield Veterinary Plasma Bank – Business Card</title>
<link href="https://fonts.googleapis.com/css2?family=Montserrat:wght@400;500;600;700;800&display=swap" rel="stylesheet">
<style>
  :root {
    --brand-red: #E61F27;
    --card-white: #FFFFFF;
    --backdrop: #E3E4E4;
    --scene-teal: #2F6F66;
    --scene-teal-dark: #1E4A45;
    --scene-wood: #8A4A2A;
    --text-white: #FFFFFF;
  }
  * { box-sizing: border-box; margin: 0; padding: 0; }
  html, body { width: 1200px; height: 900px; overflow: hidden; }
  body {
    background: var(--backdrop);
    font-family: "Montserrat", Arial, sans-serif;
    position: relative;
  }
  .card {
    position: absolute;
    top: 40px;
    width: 468px;
    height: 814px;
    border-radius: 40px;
    overflow: hidden;
    background: var(--card-white);
  }
  .card--front { left: 133px; }
  .card--back  { left: 615px; }

  /* Front card */
  .front-artwork {
    position: absolute;
    left: 0; top: 0;
    width: 100%; height: 296px;
    background:
      linear-gradient(180deg, rgba(0,0,0,0) 55%, var(--scene-wood) 100%),
      radial-gradient(circle at 60% 40%, var(--scene-teal) 0%, var(--scene-teal-dark) 100%);
  }
  .front-wordmark {
    position: absolute;
    left: 218px; top: 552px;
    transform: translate(-50%, -50%) rotate(-90deg);
    white-space: nowrap;
    display: flex;
    align-items: center;
    gap: 20px;
    color: var(--brand-red);
    font-weight: 800;
    font-size: 36px;
    line-height: 1.1;
    text-transform: uppercase;
  }
  .front-wordmark__dot {
    width: 56px; height: 56px;
    border-radius: 50%;
    background: var(--brand-red);
    flex: none;
  }

  /* Back card */
  .back-band {
    position: absolute;
    left: 0; top: 299px;
    width: 100%; bottom: 0;
    background: var(--brand-red);
  }
  .back-wordmark {
    position: absolute;
    left: 0; right: 0; top: 52px;
    text-align: center;
    color: var(--brand-red);
    font-weight: 800;
    font-size: 30px;
    line-height: 1.2;
    text-transform: uppercase;
  }
  .brand-disc {
    position: absolute;
    left: 50%; top: 334px;
    width: 166px; height: 166px;
    transform: translate(-50%, -50%);
    border-radius: 50%;
    background: var(--card-white);
  }
  .person {
    position: absolute;
    left: 0; right: 0; top: 456px;
    text-align: center;
    color: var(--text-white);
  }
  .person__name {
    font-weight: 700;
    font-size: 29px;
    line-height: 36px;
    letter-spacing: 0.2px;
  }
  .person__title {
    font-weight: 500;
    font-size: 22px;
    line-height: 30px;
    margin-top: 0;
  }
  .contact-icons {
    position: absolute;
    left: 0; right: 0; top: 554px;
    display: flex;
    justify-content: center;
    gap: 31px;
  }
  .contact-icons svg { width: 32px; height: 32px; display: block; }
  .contact-lines {
    position: absolute;
    left: 0; right: 0; top: 600px;
    text-align: center;
    color: var(--text-white);
    font-weight: 500;
    font-size: 19px;
    line-height: 30px;
  }
  .divider {
    position: absolute;
    left: 107px; right: 107px; top: 702px;
    height: 1.5px;
    background: var(--text-white);
  }
  .address {
    position: absolute;
    left: 0; right: 0; top: 718px;
    text-align: center;
    color: var(--text-white);
    font-weight: 500;
    font-size: 19px;
    line-height: 30px;
    letter-spacing: 0.6px;
  }
</style>
</head>
<body>
  <section class="card card--front">
    <div class="front-artwork" role="img" aria-label="Illustration of a veterinarian gently examining a black and white dog on a clinic table"></div>
    <div class="front-wordmark">
      <span class="front-wordmark__dot"></span>
      <span>Northfield<br>Veterinary<br>Plasma Bank</span>
    </div>
  </section>

  <section class="card card--back">
    <div class="back-band"></div>
    <div class="back-wordmark">Northfield<br>Veterinary<br>Plasma Bank</div>
    <div class="brand-disc"></div>

    <div class="person">
      <div class="person__name">DANIEL HARWOOD</div>
      <div class="person__title">Co-Founder &amp; CEO</div>
    </div>

    <div class="contact-icons">
      <svg viewBox="0 0 32 32" aria-label="Phone">
        <circle cx="16" cy="16" r="16" fill="#fff"/>
        <path d="M9 13c0-2 3-3.5 7-3.5s7 1.5 7 3.5v1.5h-3.5v-1.8c-2-.6-5-.6-7 0v1.8H9z" fill="var(--brand-red)"/>
        <rect x="10.5" y="15.5" width="11" height="7" rx="1.5" fill="var(--brand-red)"/>
      </svg>
      <svg viewBox="0 0 32 32" aria-label="Email">
        <circle cx="16" cy="16" r="16" fill="#fff"/>
        <rect x="8" y="10.5" width="16" height="11" rx="1.5" fill="none" stroke="var(--brand-red)" stroke-width="2"/>
        <path d="M8.5 11.5 16 17l7.5-5.5" fill="none" stroke="var(--brand-red)" stroke-width="2"/>
      </svg>
      <svg viewBox="0 0 32 32" aria-label="Website">
        <circle cx="16" cy="16" r="16" fill="#fff"/>
        <circle cx="16" cy="16" r="8" fill="none" stroke="var(--brand-red)" stroke-width="2"/>
        <path d="M8 16h16M16 8c-3 3-3 13 0 16M16 8c3 3 3 13 0 16" fill="none" stroke="var(--brand-red)" stroke-width="1.6"/>
      </svg>
    </div>

    <div class="contact-lines">
      <div>555-0142-3876</div>
      <div>hello@northfield-vpb.com</div>
      <div>www.northfield-vpb.com</div>
    </div>

    <div class="divider"></div>

    <div class="address">
      <div>24 Meadow Lane</div>
      <div>Fairhaven, CT 06500 USA</div>
    </div>
  </section>
</body>
</html>
```